Lantern Co. Supplement General Packaging Design

I am looking for a design template to design all of my various supplements and other products around. Meaning that this design should be able to just be able to change around words, up to a few small images, and text to suit my other various products.

The brand name is Lantern Co. and the slogan is: Legends Take Root
This is For an Apple Cider Vinegar Gummy, and include these top three things: Vegan, Gluten Free, Non-GMO somewhere in the design.

I want the design to have a luxurious feel. With some kind of design element where the logo is sort of the secondary aspect of the design.

Target Market(s)

Men age 24-45

Industry/Entity Type

Supplement

Requirements
Must have
• MUST HAVE A "vintage" LOOK AND FEEL. MUST HAVE ANOTHER design element besides the logo. (Something Vintage) MUST USE THE PROVIDED TEMPLATE A PDF IN THE FILES BELOW LABELED " TEMPLATE" and the LOGO PROVIDED under "Lantern Co. 2" OR "Lantern Co.3" whichever is better suited for the design. Bold design. Another color besides black to stand out. Use the lantern co logo which is below in the provided images. The design should go around the logo and fit the same aesthetic. The rest are for inspiration, what I like.

```html
<!DOCTYPE html>
<html lang="en">
<head>
<meta charset="utf-8">
<title>Lantern Co. – Apple Cider Vinegar Gummy Label</title>
<link rel="stylesheet" href="https://fonts.googleapis.com/css2?family=Bebas+Neue&family=Arimo:wght@400;700&family=Archivo+Black&display=swap">
<style>
  :root{
    --page:#f2f2f4;
    --red:#d9232b;
    --red-deep:#b81d24;
    --charcoal:#3b3c3e;
    --ink:#1b1b1b;
    --white:#ffffff;
  }
  *{box-sizing:border-box;margin:0;padding:0}
  html,body{width:1200px;height:1065px;overflow:hidden;background:var(--page)}
  .canvas{position:relative;width:1200px;height:1065px}
  .label{
    position:absolute;left:20px;top:388px;width:1364px;height:340px;
    transform:scale(0.85);transform-origin:top left;
    background:var(--red);font-family:"Arimo",Arial,sans-serif;color:var(--white);
    box-shadow:0 6px 14px rgba(0,0,0,.25);overflow:hidden;
  }
  .barcode-zone{
    position:absolute;left:0;top:0;width:70px;height:340px;background:var(--white);
    border-right:2px solid var(--ink);
  }
  .barcode-zone span{
    position:absolute;left:35px;top:170px;transform:translate(-50%,-50%) rotate(90deg);
    white-space:nowrap;color:var(--ink);font-size:17px;
  }
  .directions{position:absolute;left:88px;top:18px;width:279px;font-size:10.5px;line-height:1.25}
  .directions p{margin-bottom:12px;text-align:justify}
  .directions b{font-weight:700}
  .fda-note{border:1.5px solid var(--white);padding:5px 7px;margin-bottom:12px;font-size:11px;text-align:justify}
  .maker-label{font-size:10px;margin-bottom:7px}
  .maker-box{background:var(--white);color:var(--ink);border:1.5px solid var(--ink);height:38px;display:flex;align-items:center;justify-content:center;font-size:10.5px}
  .front-panel{position:absolute;left:400px;top:0;width:588px;height:215px}
  .front-panel svg{position:absolute;inset:0}
  .est{position:absolute;left:245px;top:14px;width:80px;text-align:center;font-family:"Bebas Neue",sans-serif;font-size:17px;letter-spacing:1px;transform:rotate(-4deg)}
  .brand{position:absolute;left:80px;top:96px;width:400px;text-align:center;font-family:"Bebas Neue",sans-serif;font-size:62px;line-height:1;letter-spacing:1px;color:var(--white)}
  .brand-dot{display:inline-block;width:10px;height:10px;border-radius:50%;background:var(--white);margin-left:4px;vertical-align:baseline}
  .slogan{position:absolute;left:60px;top:160px;width:440px;text-align:center;font-family:"Bebas Neue",sans-serif;font-size:40px;line-height:1;letter-spacing:1px;color:var(--red)}
  .claims-ribbon{position:absolute;left:825px;top:0;width:60px;height:205px}
  .claim{position:absolute;left:0;width:60px;text-align:center;font-size:9px;color:var(--white)}
  .claim i{display:block;width:38px;height:38px;margin:0 auto 3px;border-radius:50%;border:2.5px solid var(--white)}
  .rule{position:absolute;left:445px;top:215px;width:485px;height:7px;border-top:3px solid var(--charcoal);border-bottom:1.5px solid var(--charcoal)}
  .product-name{position:absolute;left:400px;top:245px;width:560px;text-align:center;font-family:"Bebas Neue",sans-serif;font-size:44px;letter-spacing:1.5px;line-height:1}
  .product-type{position:absolute;left:400px;top:300px;width:560px;text-align:center;font-family:"Bebas Neue",sans-serif;font-size:19px;letter-spacing:1px}
  .facts{position:absolute;left:1017px;top:25px;width:263px;height:293px;border:1.5px solid var(--white);padding:4px 6px;font-size:10px;line-height:1.15}
  .facts h2{font-family:"Archivo Black",sans-serif;font-size:19px;font-weight:400;letter-spacing:.5px;line-height:1.1}
  .facts .serving{font-weight:700;font-size:10.5px;padding-bottom:6px;border-bottom:5px solid var(--white)}
  .facts .head{text-align:right;font-weight:700;padding:4px 0 2px;border-bottom:2.5px solid var(--white)}
  .row{display:grid;grid-template-columns:1fr auto 34px;gap:4px;border-bottom:.8px solid var(--white);padding:1.5px 0}
  .row span:nth-child(2),.row span:nth-child(3){text-align:right}
  .row.indent span:first-child{padding-left:10px}
  .row.indent2 span:first-child{padding-left:16px}
  .facts .foot{border-top:4px solid var(--white);margin-top:8px;padding-top:4px}
  .ingredients{position:absolute;left:1290px;top:18px;width:300px;height:50px;transform-origin:top left;transform:translate(0,302px) rotate(-90deg);font-size:10px;line-height:1.2}
</style>
</head>
<body>
<main class="canvas">
  <section class="label">
    <div class="barcode-zone"><span>Bar-Code Zone</span></div>

    <div class="directions">
      <p><b>Suggested Use:</b> Take one (1) gummy daily or as directed by a healthcare professional.</p>
      <p><b>Caution:</b> If you are pregnant, nursing, taking any medications or have any medical condition, consult your doctor before use. Discontinue use and consult your doctor if any adverse reactions occur.</p>
      <p>KEEP OUT OF REACH OF CHILDREN. STORE AT ROOM TEMPERATURE.</p>
      <p>ALLERGEN WARNING: This product contains tree nuts (coconut).</p>
      <div class="fda-note">†These statements have not been evaluated by the FDA. This product is not intended to diagnose, cure, treat or prevent any disease.</div>
      <div class="maker-label">Manufactured for:</div>
      <div class="maker-box">Manufactured for Zone</div>
    </div>

    <div class="front-panel">
      <svg viewBox="0 0 588 215" width="588" height="215" aria-hidden="true">
        <path d="M36 0 H552 C602 55 602 150 560 215 H28 C-14 150 -14 55 36 0 Z" fill="var(--charcoal)"/>
      </svg>
      <div class="est">EST. 2020</div>
      <div class="brand">LANTERN CO.<span class="brand-dot"></span></div>
      <div class="slogan">LEGENDS TAKE ROOT</div>
    </div>

    <div class="claims-ribbon">
      <svg viewBox="0 0 60 205" width="60" height="205" style="position:absolute;inset:0" aria-hidden="true">
        <path d="M0 0 H60 V195 L30 205 L0 195 Z" fill="var(--red)" stroke="var(--red-deep)" stroke-width="1"/>
      </svg>
      <div class="claim" style="top:22px"><i></i>Vegan</div>
      <div class="claim" style="top:76px"><i></i>Gluten free</div>
      <div class="claim" style="top:132px"><i></i>Non-GMO</div>
    </div>

    <div class="rule"></div>
    <div class="product-name">APPLE CIDER VINEGAR GUMMY</div>
    <div class="product-type">DIETARY SUPPLEMENT</div>

    <div class="facts">
      <h2>SUPPLEMENT FACTS</h2>
      <div class="serving">Serving Size: 1 Gummy<br>Servings Per Container: 60</div>
      <div class="head">Amount Per Serving &nbsp;% DV</div>
      <div class="row"><span>Calories</span><span>10</span><span></span></div>
      <div class="row"><span>Total Carbohydrates</span><span>3 g</span><span>&lt;1%</span></div>
      <div class="row indent"><span>Total Sugars</span><span>2 g</span><span>**</span></div>
      <div class="row indent2"><span>Includes 2 g Added Sugars</span><span></span><span>4%</span></div>
      <div class="row"><span>Vitamin B-6 (as Pyridoxine HCl)</span><span>0.5 mg</span><span>29%</span></div>
      <div class="row"><span>Folate (120 mcg Folic Acid)</span><span>200 mcg DFE</span><span>50%</span></div>
      <div class="row"><span>Vitamin B-12 (as Cyanocobalamin)</span><span>1.2 mcg</span><span>50%</span></div>
      <div class="row"><span>Iodine (as Potassium Iodide)</span><span>50 mcg</span><span>33%</span></div>
      <div class="row"><span>Apple Cider Vinegar Powder (fruit)<br>(providing 5% total acid)</span><span>500 mg</span><span>**</span></div>
      <div class="row"><span>Pomegranate Juice Powder</span><span>40 mcg</span><span>**</span></div>
      <div class="row"><span>Beet Root Juice Powder</span><span>40 mcg</span><span>**</span></div>
      <div class="foot">* % Daily Value Based on 2,000 Calorie Diet<br>** Daily Value Not Established</div>
    </div>

    <div class="ingredients"><b>Other Ingredients:</b> Glucose Syrup, Sugar, Glucose, Pectin, Sodium Citrate, Citric Acid, Natural Apple Flavor, Vegetable Oil, Liquid Apple Cider Vinegar, Purple carrot Juice Concentrate and Beta Carotene.</div>
  </section>
</main>
</body>
</html>
```